Webdesign für Adressvalidierung
Zielgruppe
Was macht die Firma: Addressvalidierung zur Steigerung der Datenqualität vom Spezialisten.
Zielgruppe: B2B - alle Branchen, die auf Datenqualität setzen.
Aufgabenstellung
Die Herausforderung besteht darin, die umfangreichen Textinhalte optisch ansprechend darzustellen. Hierfür sollten die Beispiel-Designs unbedingt die vorgefertigten Texte für (Meta-Titel, Sub-Headline, Seitenüberschrift etc.) berücksichtigen, damit wir eine genaue Vorstellung über die Website erhalten.

```html
<!DOCTYPE html>
<html lang="de">
<head>
<meta charset="utf-8">
<title>ADRESSIO – Komplettlösungen für professionelle Adressvalidierung</title>
<link rel="stylesheet" href="https://fonts.googleapis.com/css2?family=Roboto:wght@400;500;700&display=swap">
<style>
:root{
  --blue:#0562b5;
  --ink:#333;
  --white:#fff;
  --placeholder:#edf0f3;
}
*{margin:0;padding:0;box-sizing:border-box}
html,body{width:1200px;height:2887px;overflow:hidden;background:var(--white);font-family:'Roboto',sans-serif;color:var(--ink)}
.page{position:relative;width:1200px;height:2887px}
.abs{position:absolute}
b{font-weight:700;color:#222}

/* header */
.header{top:0;left:0;width:1200px;height:85px;background:var(--white)}
.brand{left:92px;top:30px;display:flex;align-items:center;gap:8px;color:var(--blue);font-weight:700;font-size:20px;letter-spacing:.5px}
.brand-dot{width:14px;height:14px;border-radius:50%;background:var(--blue);display:block}
.nav{left:261px;top:51px;display:flex;gap:26px;font-size:12px;color:#555}
.nav .active{color:var(--blue);font-weight:700}
.search{left:756px;top:26px;width:224px;height:33px;border:1px solid #dde2e7;border-radius:17px;font-size:11px;color:#9aa3ad;padding:10px 15px}
.search svg{position:absolute;right:14px;top:8px}
.btn{display:inline-block;background:var(--blue);color:var(--white);font-weight:700;font-size:12px;border-radius:18px;text-align:center}
.signup{left:1007px;top:25px;width:102px;height:34px;line-height:34px}

/* hero */
.hero{top:85px;left:0;width:1200px;height:435px;background:linear-gradient(135deg,#0a66b8,#0560b2 60%,#0a5fae)}
.tag{left:87px;top:177px;background:var(--white);color:#222;font-weight:500;font-size:15px;padding:3px 12px}
.hero-title{left:87px;top:214px;color:var(--white);font-weight:700;font-size:58px;line-height:69px;width:1050px}

.card{background:var(--white);border-radius:10px;box-shadow:0 4px 16px rgba(0,0,0,.1);padding:42px 34px 0 35px}
.card h2{color:var(--blue);font-size:22px;line-height:29px;font-weight:700;margin-bottom:22px}
.card p{font-size:10.5px;line-height:16px;color:#444;margin-bottom:16px}
.card-left{left:87px;top:417px;width:499px;height:319px}
.card-right{left:627px;top:417px;width:499px;height:322px;padding-left:34px}

/* facts */
.facts-title{top:803px;left:0;width:1218px;text-align:center;color:var(--blue);font-size:22px;font-weight:700}
.fact{width:316px;height:199px;background:var(--white);border-radius:8px;box-shadow:0 2px 14px rgba(0,0,0,.08);text-align:center;padding-top:34px}
.fact svg{display:block;margin:0 auto 18px}
.fact p{font-size:15.5px;line-height:22px;font-weight:500;color:#333;letter-spacing:.3px}

/* text section */
.why-title{left:90px;top:1357px;color:var(--blue);font-size:22px;line-height:29px;font-weight:700}
.col{width:472px;font-size:10.3px;line-height:16.3px;color:#555}
.col p{margin-bottom:16px}
.col-left{left:90px;top:1428px}
.col-right{left:627px;top:1428px}
.btn-contact{width:209px;height:34px;line-height:34px}

/* testimonial */
.quote-band{top:1779px;left:0;width:1200px;height:289px;background:linear-gradient(135deg,#0a66b8,#0560b2)}
.arrow{width:33px;height:33px;border-radius:50%;background:var(--white);display:flex;align-items:center;justify-content:center}
.avatar{left:210px;top:1854px;width:140px;height:140px;border-radius:50%;background:var(--placeholder);display:flex;align-items:center;justify-content:center}
.quote{left:459px;top:1871px;width:470px;color:var(--white);font-size:10.5px;line-height:16.3px}
.quote-name{left:459px;top:1950px;color:var(--white);font-size:15px;font-weight:700}
.quote-role{left:459px;top:1970px;color:#cfe0f2;font-size:9.5px}

/* experts */
.experts-title{left:87px;top:2152px;color:var(--blue);font-size:22px;font-weight:700}
.experts-text{left:87px;top:2197px;width:480px;font-size:10.3px;line-height:16.3px;color:#555}
.team{width:158px;height:158px;border-radius:50%;background:var(--placeholder);display:flex;align-items:center;justify-content:center;top:2143px}

/* trust */
.trust{top:2428px;left:0;width:1200px;height:215px;background:linear-gradient(135deg,#0a66b8,#0560b2)}
.trust-label{top:2491px;left:0;width:1200px;text-align:center;color:var(--white);font-size:11px;font-weight:700}
.partners{top:2542px;left:232px;display:flex;gap:74px}
.partner{display:flex;align-items:center;gap:8px;color:var(--white);font-size:21px;font-weight:700}
.partner i{width:14px;height:14px;background:var(--white);display:block}

/* footer */
.foot-brand{left:86px;top:2730px;display:flex;align-items:center;gap:9px;color:var(--blue);font-weight:700;font-size:24px;letter-spacing:.6px}
.foot-brand .brand-dot{width:18px;height:18px}
.socials{left:84px;top:2793px;display:flex;gap:11px}
.socials i{width:20px;height:20px;border-radius:50%;background:var(--blue);display:block}
.copyright{left:110px;top:2829px;font-size:7.5px;color:#666}
.foot-col h4{font-size:8px;font-weight:700;color:#555;margin-bottom:17px;letter-spacing:.3px}
.foot-col a{display:block;font-size:10.5px;color:var(--blue);text-decoration:none;margin-bottom:9px}
</style>
</head>
<body>
<div class="page">

  <header class="abs header">
    <div class="abs brand"><span class="brand-dot"></span><span>ADRESSIO</span></div>
    <nav class="abs nav"><span class="active">Overview</span><span>Features</span><span>Forums</span><span>Downloads</span></nav>
    <div class="abs search">Search here
      <svg width="17" height="17" viewBox="0 0 17 17"><circle cx="7" cy="7" r="5.5" fill="none" stroke="#8a96a3" stroke-width="2"/><line x1="11" y1="11" x2="15.5" y2="15.5" stroke="#8a96a3" stroke-width="2.2" stroke-linecap="round"/></svg>
    </div>
    <span class="abs btn signup">Sign up</span>
  </header>

  <section class="abs hero"></section>
  <div class="abs tag">Der wichtigste Kontakt: Ihr Kunde von morgen</div>
  <h1 class="abs hero-title">Komplettlösungen für<br>professionelle Adressvalidierung</h1>

  <article class="abs card card-left">
    <h2>Automatisch mehr Kundenkontakte:<br>Adressvalidierung wirkt</h2>
    <p>Eine hohe <b>Datenqualität</b> ist der entscheidende <b>Wettbewerbsvorteil</b> im digitalisierten Marktumfeld. Unternehmen können <b>kostbare Ressourcen</b> treffsicher ausrichten, effizientkommunizieren und einfach <b>mehr Kunden sicher erreichen.</b></p>
    <p>Damit können Waren und Dienstleistungen einfach <b>besser verkauft</b>, und Geschäftsergebnisse <b>gezielt gesteigert werden.</b> Wir liefern Lösungen für die dafür nötige Adressprüfung und helfen Ihnen mit bewährten Prozessen zur <b>professionellen Adressvalidierung.</b></p>
    <p>Kontaktieren Sie uns. Wir sind als Ansprechpartner für Sie da.</p>
  </article>

  <article class="abs card card-right">
    <h2>Erfolgsfaktor Adressvalidierung:<br>Bessere Kontakte zur richtigen Zeit</h2>
    <p>Die Vorteile einer professionellen Adressprüfung lassen sich <b>wirkungsvoll</b> Zusammenfassen: Die Information zu <b>Produkten, Leistungen und Lösungen</b> erreicht auch die richtigen Empfänger und sichert dadurch bessere <b>Auftragslagen und Verkaufszahlen</b>.</p>
    <p>Mit validen Daten erzielen kostspielige Direktmarketing Maßnahmen also einfach ein <b>stärkeres Ergebnis.</b> Das überzeugt nicht nur die Marketingleitungen. Auch für die Geschäftsführung ist ein maximaler <b>Return of Investment (ROI)</b> von zentralem Interesse.</p>
    <p>Konkret liefert eine <b>professionelle Adressprüfung</b> also die Möglichkeit mit derselben Investition in Marketing, Akquise und Vertrieb einfach mehr zu erreichen.</p>
  </article>

  <h2 class="abs facts-title">Adressprüfung: Wichtiges kurz notiert</h2>

  <svg width="0" height="0" style="position:absolute">
    <defs>
      <g id="gear">
        <circle cx="35" cy="35" r="19" fill="none" stroke="#0562b5" stroke-width="9" stroke-dasharray="7 5"/>
        <circle cx="35" cy="35" r="15" fill="none" stroke="#0562b5" stroke-width="6"/>
        <path d="M8 28 A28 28 0 0 1 50 9" fill="none" stroke="#0562b5" stroke-width="3"/>
        <path d="M62 42 A28 28 0 0 1 20 61" fill="none" stroke="#0562b5" stroke-width="3"/>
        <path d="M46 4 L54 10 L45 14Z" fill="#0562b5"/>
        <path d="M24 66 L16 60 L25 56Z" fill="#0562b5"/>
      </g>
    </defs>
  </svg>

  <div class="abs fact" style="left:92px;top:866px">
    <svg width="70" height="70" viewBox="0 0 70 70"><use href="#gear"/></svg>
    <p>Automatische Anschriftenprüfung &amp;<br>Integration fehlender Daten</p>
  </div>
  <div class="abs fact" style="left:441px;top:866px">
    <svg width="70" height="70" viewBox="0 0 70 70"><rect x="6" y="14" width="58" height="44" rx="5" fill="#0562b5"/><path d="M8 18 L35 40 L62 18" fill="none" stroke="#fff" stroke-width="3.5"/></svg>
    <p>Prüfung der E-Mail-Adresse,<br>Postanschrift oder anderer Felder</p>
  </div>
  <div class="abs fact" style="left:794px;top:866px">
    <svg width="70" height="70" viewBox="0 0 70 70"><circle cx="35" cy="35" r="25" fill="#0562b5" stroke="#0562b5" stroke-width="12" stroke-dasharray="8 5"/><path d="M23 35 L32 44 L48 27" fill="none" stroke="#fff" stroke-width="5" stroke-linecap="round" stroke-linejoin="round"/></svg>
    <p>Adresskorrektur basierend auf<br>aktualisierten Referenzdaten</p>
  </div>
  <div class="abs fact" style="left:92px;top:1107px">
    <svg width="70" height="70" viewBox="0 0 70 70"><use href="#gear"/></svg>
    <p>Leistungsfähige Software für ein<br>zeitgemäßes Daten Management</p>
  </div>
  <div class="abs fact" style="left:443px;top:1107px">
    <svg width="70" height="70" viewBox="0 0 70 70"><use href="#gear"/></svg>
    <p>Bewährte Funktion &amp;<br>vielfältig vorteilhafte Verwendung</p>
  </div>
  <div class="abs fact" style="left:794px;top:1107px">
    <svg width="70" height="70" viewBox="0 0 70 70"><use href="#gear"/></svg>
    <p>Persönliche Beratung:<br>Direktweg zu geprüften Adressen</p>
  </div>

  <h2 class="abs why-title">Wie wichtig sind Kundenkontakte<br>für ein modernes Business?</h2>
  <div class="abs col col-left">
    <p>Wie wichtig sind Kunden ganz allgemein für ein Geschäft? Beide Fragen sind trivial, denn nur sehr wenige Unternehmen und Geschäftsmodelle kommen ohne Kunden aus. Zudem haben erfolgreiche Marktteilnehmer bereits erkannt, dass <b>hochwertige und vollständige Adressdate</b>n zur richtigen Zeit im digitalen Zeitalter noch wichtiger geworden sind.</p>
    <p>Jeder Auftrag kann heute einfach, schnell und vor allem auch überregional platziert werden. Wenn Unternehmen mit Ihren Lösungen nicht zur richtigen Zeit für <b>potentielle Auftraggeber</b> da sind, dann geht der Auftrag ganz einfach an ein anderes Unternehmen oder in ein anderes Land. Der Einsatz und die Anwendung falscher Adressen oder fehlerhafter Adressen verursachen sinnlose Kosten und Ausgaben. Gleichzeitig bleiben <b>potentiell wichtige Kundinnen und Kunden</b> unerreicht, nur weil sie beispielsweise eine neue Adresse haben. Mit geprüften und vollständig aktuellen Adressen lassen sich hingegen <b>bewährte Vertriebskampagnen organisieren</b>, die rechtzeitig die nötige Reichweite sicherstellen.</p>
    <p>Wichtige Informationen erreichen Zielgruppen rechtzeitig und es werden Ergebnisse erzielt, die rundum überzeugen</p>
  </div>
  <div class="abs col col-right">
    <p>Vor diesem Hintergrund sind valide Adressdaten und Datensätze ein <b>wichtiger Rohstoff</b> unserer digitalisierten Wirtschaft. Mit einer vollständigen Adressprüfung oder einem professionellen Adress-Check können wir diesen wichtigen <b>Datenbestand prüfen, Fehler und falsche Daten erkennen</b>, Daten mit aktuellen Adressen abgleichen, eine <b>zielführende Adresskorrektur</b> vornehmen und diesen entscheidenden Rohstoff modernen Marketings also aufwerten und aufbereiten.</p>
    <p>Wenn Sie also Kundenkontakte verwalten, eine Direktmarketing-Kampagne planen oder eine Adressbereinigung alter Datenbestände vornehmen möchten, haben wir das <b>richtige System</b> für Sie.</p>
    <p>Mit einer Adresskorrektur und  Prüfung anhand unserer Tools werten Sie Ihren Bestand clever und zielführend auf.</p>
    <p><b>Kontaktieren Sie uns. Wir lassen Ihnen gerne weitere Informationen zukommen und beraten Sie persönlich, sicher und diskret.</b></p>
    <span class="btn btn-contact">Jetzt kontakt aufnehmen</span>
  </div>

  <section class="abs quote-band"></section>
  <div class="abs arrow" style="left:127px;top:1913px"><svg width="10" height="12" viewBox="0 0 10 12"><path d="M7 1 L2 6 L7 11" fill="none" stroke="#333" stroke-width="1.8"/></svg></div>
  <div class="abs arrow" style="left:1062px;top:1913px"><svg width="10" height="12" viewBox="0 0 10 12"><path d="M3 1 L8 6 L3 11" fill="none" stroke="#333" stroke-width="1.8"/></svg></div>
  <div class="abs avatar" role="img" aria-label="Porträtfoto der zitierten Person">
    <svg width="36" height="36" viewBox="0 0 36 36"><rect x="2" y="4" width="32" height="28" rx="3" fill="none" stroke="#a8b2bd" stroke-width="2.2"/><circle cx="12" cy="13" r="3" fill="none" stroke="#a8b2bd" stroke-width="2"/><path d="M4 28 L14 19 L21 25 L26 21 L33 27" fill="none" stroke="#a8b2bd" stroke-width="2"/></svg>
  </div>
  <p class="abs quote">Currently, Norvik Motors sells six sedans and coupes in North America with the Arla, Brisk, Corva, Delta, Esker and Fjord. This lineup hits multiple segments from the compact Arla to the mid-size Brisk, Corva and Delta to the full-size Fjord.</p>
  <div class="abs quote-name">Lena Marquardt</div>
  <div class="abs quote-role">Author at Kestrel Store</div>

  <h2 class="abs experts-title">Sprechen Sie mit unseren Experten</h2>
  <p class="abs experts-text">Lassen Sie sich unverbindlich beraten, wie auch Ihre Geschäftsprozesse mit dem  ADRESSIO optimiert werden können. Wir zeigen Ihnen individuelle Lösungsansätze und entwickeln gemeinsam mit Ihnen eine Strategie, wie Sie Ihr Tagesgeschäft plattformgestützt optimieren können.</p>
  <span class="abs btn btn-contact" style="left:87px;top:2272px">Jetzt Kontakt aufnehmen</span>
  <div class="abs team" style="left:654px" role="img" aria-label="Porträtfoto Experte 1"><svg width="40" height="40" viewBox="0 0 36 36"><rect x="2" y="4" width="32" height="28" rx="3" fill="none" stroke="#a8b2bd" stroke-width="2.2"/><circle cx="12" cy="13" r="3" fill="none" stroke="#a8b2bd" stroke-width="2"/><path d="M4 28 L14 19 L21 25 L26 21 L33 27" fill="none" stroke="#a8b2bd" stroke-width="2"/></svg></div>
  <div class="abs team" style="left:804px" role="img" aria-label="Porträtfoto Experte 2"><svg width="40" height="40" viewBox="0 0 36 36"><rect x="2" y="4" width="32" height="28" rx="3" fill="none" stroke="#a8b2bd" stroke-width="2.2"/><circle cx="12" cy="13" r="3" fill="none" stroke="#a8b2bd" stroke-width="2"/><path d="M4 28 L14 19 L21 25 L26 21 L33 27" fill="none" stroke="#a8b2bd" stroke-width="2"/></svg></div>
  <div class="abs team" style="left:954px" role="img" aria-label="Porträtfoto Experte 3"><svg width="40" height="40" viewBox="0 0 36 36"><rect x="2" y="4" width="32" height="28" rx="3" fill="none" stroke="#a8b2bd" stroke-width="2.2"/><circle cx="12" cy="13" r="3" fill="none" stroke="#a8b2bd" stroke-width="2"/><path d="M4 28 L14 19 L21 25 L26 21 L33 27" fill="none" stroke="#a8b2bd" stroke-width="2"/></svg></div>

  <section class="abs trust"></section>
  <div class="abs trust-label">Diese Firmen vertrauen uns</div>
  <div class="abs partners">
    <span class="partner"><i></i>Company</span>
    <span class="partner"><i></i>Company</span>
    <span class="partner"><i></i>Company</span>
    <span class="partner"><i></i>Company</span>
  </div>

  <footer>
    <div class="abs foot-brand"><span class="brand-dot"></span><span>ADRESSIO</span></div>
    <div class="abs socials"><i></i><i></i><i></i><i></i><i></i></div>
    <div class="abs copyright">Copyright © Jonas Feld</div>
    <div class="abs foot-col" style="left:382px;top:2696px"><h4>PRODUCTS</h4><a>Features</a><a>Personal License</a><a>Business License</a><a>Pricing Options</a></div>
    <div class="abs foot-col" style="left:616px;top:2696px"><h4>COMPANY</h4><a>About</a><a>Careers</a><a>Blog</a><a>Contact</a></div>
    <div class="abs foot-col" style="left:849px;top:2696px"><h4>SUPPORT</h4><a>Support Center</a><a>Help Desk</a><a>FAQ</a></div>
  </footer>

</div>
</body>
</html>
```